KRV Business Cards

We are a local commercial development company based in Silicon Valley and we would like a new business card. I've attached a copy of our company brochure to give a flavor of what we do, our logo, info company colors/graphics, and our current business card. We don't necessarily need a crazy makeover, but would like something that feels a little bit more "fresh" and modern (we've had the same business card design for 15+ years), but still in keeping with our overall brand -- clean, high-quality, modern but timeless. Would like to add our website to the info on the card (www.velmara.com) and would like the flexibility for some folks to have an efax number listed and some not to have that included (without it looking like there is a hole).

```html
<!DOCTYPE html>
<html lang="en">
<head>
<meta charset="utf-8">
<title>KRV Business Cards</title>
<link href="https://fonts.googleapis.com/css2?family=Cinzel:wght@400;600&family=Lexend:wght@400;500&display=swap" rel="stylesheet">
<style>
  :root{
    --backdrop:#2b2c2e;
    --brand-blue:#34546e;
    --ink-navy:#2c4a63;
    --paper:#fbfcfd;
    --white:#ffffff;
    --photo-light:#eef2f5;
    --photo-mid:#dbe3ea;
  }
  *{margin:0;padding:0;box-sizing:border-box}
  html,body{width:930px;height:1200px;overflow:hidden;background:var(--backdrop)}
  .sheet{position:relative;width:930px;height:1200px}
  .card{position:absolute;left:85px;width:760px;height:434px;border-radius:6px;overflow:hidden}
  .card--front{top:95px;background:var(--brand-blue);color:var(--white)}
  .card--back{top:670px;background:var(--paper);color:var(--ink-navy)}

  .wordmark{font-family:"Cinzel",serif;font-weight:400;letter-spacing:1px;line-height:1}
  .tagline{font-family:"Lexend",sans-serif;font-weight:500;text-transform:uppercase;letter-spacing:1.5px}

  .front-brand{position:absolute;left:150px;top:140px}
  .front-brand .wordmark{font-size:62px}
  .front-brand .tagline{font-size:12px;margin-top:6px}
  .front-rule{position:absolute;left:322px;top:268px;width:116px;height:5px;background:var(--white)}
  .front-web{position:absolute;left:0;right:0;top:300px;text-align:center;font-family:"Lexend",sans-serif;font-size:15px;letter-spacing:3px}

  .back-photo{position:absolute;inset:60px 0 0 0;background:linear-gradient(180deg,var(--photo-light) 0%,var(--photo-mid) 55%,var(--photo-light) 100%);opacity:.75}
  .back-brand{position:absolute;left:44px;top:74px}
  .back-brand .wordmark{font-size:44px}
  .back-brand .tagline{font-size:9px;margin-top:5px}
  .person{position:absolute;right:48px;top:60px;text-align:right}
  .person__name{font-family:"Cinzel",serif;font-size:25px;letter-spacing:1px}
  .person__role{font-family:"Lexend",sans-serif;font-weight:500;font-size:12px;letter-spacing:2px;text-transform:uppercase;margin-top:2px;margin-right:60px}
  .contacts{position:absolute;left:350px;top:170px;list-style:none;font-family:"Lexend",sans-serif;font-weight:500;font-size:15px;letter-spacing:1.5px}
  .contacts li{display:flex;align-items:center;height:24px}
  .contacts svg{width:14px;height:14px;margin-right:12px;fill:var(--ink-navy)}
  .contacts .plain{padding-left:26px}
  .address{position:absolute;left:44px;bottom:56px;font-family:"Lexend",sans-serif;font-weight:500;font-size:15px;letter-spacing:.5px}
</style>
</head>
<body>
<main class="sheet">
  <section class="card card--front">
    <div class="front-brand">
      <div class="wordmark">VELMARA</div>
      <div class="tagline">Development Company, LLC</div>
    </div>
    <div class="front-rule"></div>
    <div class="front-web">www.velmara.com</div>
  </section>

  <section class="card card--back">
    <div class="back-photo" role="img" aria-label="Faded photograph of a commercial building storefront"></div>
    <div class="back-brand">
      <div class="wordmark">VELMARA</div>
      <div class="tagline">Development Company, LLC</div>
    </div>
    <div class="person">
      <div class="person__name">Elena J. Marsh</div>
      <div class="person__role">Partner</div>
    </div>
    <ul class="contacts">
      <li><svg viewBox="0 0 24 24"><path d="M6.6 10.8a15 15 0 0 0 6.6 6.6l2.2-2.2a1 1 0 0 1 1-.25 11.4 11.4 0 0 0 3.6.57 1 1 0 0 1 1 1V20a1 1 0 0 1-1 1A17 17 0 0 1 3 4a1 1 0 0 1 1-1h3.5a1 1 0 0 1 1 1c0 1.25.2 2.45.57 3.57a1 1 0 0 1-.25 1z"/></svg>555-210-4816, 555-210-4890</li>
      <li><svg viewBox="0 0 24 24"><rect x="6" y="2" width="12" height="20" rx="2"/></svg>555-387-2209</li>
      <li><svg viewBox="0 0 24 24"><path d="M2 5h20v14H2z M3 6l9 7 9-7" /></svg>elena@velmara.com</li>
      <li><svg viewBox="0 0 24 24"><circle cx="12" cy="12" r="10"/></svg>www.velmara.com</li>
    </ul>
    <div class="address">62 Linden Row, Cedar Point, California 90000</div>
  </section>
</main>
</body>
</html>
```